Marrowind Estates Wine Label

We are seeking a new brand label image for our 20+ year old wine brand Marrowind. Our current label is very basic and we are seeking something ELEGANT and MODERN but also MORE EYE-CATCHING.

The label art needs to incorporate our existing fairy image (please see attached images) which can be in color or in black and white line art.

The fairy image should be a smaller component of the design—not the main aspect—and should be placed as a discreet logo somewhere on the label.

We want a more modern, elegant and exciting look. One that builds on the Brandname Marrowind downplays the ICON Faerie but enhances our brand name's equity.

Update: May 26
1. Logo PSD file attached
-Logo File/Font info: For 600dpi resolution, MARROWIND is 40pt Berhard Modern BT (in bold, standard spacing). ESTATES is 13pt with 178% spacing)

2. The size is variable, and dependent on whether we do 1 larger (longer) label that wraps around the bottle, or 2 separate labels. Our current labels are 4.5” square for front and 3.5” for back (see file attached).

additional notes: we can put the alcohol and volume size on the back label. And/or we can make a “front” label that is legally submitted as the back label (and vice versa… see attached Tamber Owlet labels).

Target Market(s)

Wine drinkers!

Font styles to use
Other font styles liked:
• Our logo text is Bernhard Modern Bold

Requirements
Nice to have
• See description

```html
<!DOCTYPE html>
<html lang="en">
<head>
<meta charset="utf-8">
<title>Marrowind Estates Wine Labels</title>
<link rel="stylesheet" href="https://fonts.googleapis.com/css2?family=Cormorant+Garamond:wght@400;500&family=Montserrat:wght@500;600&family=IBM+Plex+Sans:wght@400;600&display=swap">
<style>
  :root {
    --backdrop: #ecebec;
    --navy-light: #48535f;
    --navy-dark: #1e252e;
    --paper: #f5f5f3;
    --gold: #b59c5e;
    --title-on-dark: #d9dde2;
    --sub-on-dark: #8b949e;
    --ink: #2b3038;
    --emblem-on-dark: #56606b;
    --emblem-on-light: #e2e3e3;
    --year-on-dark: #9aa3ad;
    --year-on-light: #6f7780;
  }
  * { box-sizing: border-box; margin: 0; padding: 0; }
  html, body { width: 1200px; height: 891px; overflow: hidden; }
  body {
    background: radial-gradient(ellipse at 50% 40%, #f7f7f7 0%, var(--backdrop) 100%);
    display: flex; align-items: center; justify-content: center; gap: 70px;
  }
  .label {
    width: 380px; height: 740px; position: relative; text-align: center;
    box-shadow: 0 10px 30px rgba(0,0,0,.12);
  }
  .label--red { background: linear-gradient(120deg, var(--navy-light) 0%, var(--navy-dark) 100%); }
  .label--white { background: var(--paper); }
  .brand { position: absolute; top: 60px; left: 0; right: 0; }
  .brand__name {
    display: inline-block;
    font-family: "Cormorant Garamond", serif; font-weight: 400;
    font-size: 62px; letter-spacing: .04em; line-height: 1;
    transform: scaleX(.62); transform-origin: center;
  }
  .brand__sub {
    font-family: "Montserrat", sans-serif; font-weight: 500;
    font-size: 10px; letter-spacing: .22em; margin-top: 10px;
  }
  .label--red .brand__name { color: var(--title-on-dark); }
  .label--red .brand__sub { color: var(--sub-on-dark); }
  .label--white .brand__name { color: var(--ink); }
  .label--white .brand__sub { color: #7c838b; }
  .emblem {
    position: absolute; top: 250px; left: 90px; width: 200px; height: 200px;
    border-radius: 50%;
  }
  .label--red .emblem { background: var(--emblem-on-dark); }
  .label--white .emblem { background: var(--emblem-on-light); }
  .varietal {
    position: absolute; top: 515px; left: 0; right: 0;
    font-family: "Montserrat", sans-serif; font-weight: 600;
    font-size: 18px; letter-spacing: .62em; padding-left: .62em;
  }
  .label--red .varietal { color: #eef0f2; }
  .label--white .varietal { color: var(--ink); }
  .region {
    position: absolute; top: 562px; left: 0; right: 0;
    font-family: "Montserrat", sans-serif; font-weight: 500;
    font-size: 10px; letter-spacing: .4em; padding-left: .4em; color: var(--gold);
  }
  .details {
    position: absolute; bottom: 44px; left: 0; right: 0;
    display: flex; align-items: baseline; justify-content: center; gap: 22px;
    font-family: "IBM Plex Sans", sans-serif;
  }
  .details__small { font-size: 9px; }
  .details__year { font-size: 42px; font-weight: 600; letter-spacing: .06em; }
  .label--red .details__small { color: #c7ccd2; }
  .label--red .details__year { color: var(--year-on-dark); }
  .label--white .details__small { color: #a4a9ae; }
  .label--white .details__year { color: var(--year-on-light); }
</style>
</head>
<body>
  <section class="label label--red">
    <header class="brand">
      <h1 class="brand__name">MARROWIND</h1>
      <p class="brand__sub">ESTATES</p>
    </header>
    <div class="emblem" role="img" aria-label="Varietal emblem with small fairy mark"></div>
    <h2 class="varietal">NORTON</h2>
    <p class="region">HALDEN RESERVE VIRGINIA</p>
    <div class="details">
      <span class="details__small">13,1% VOL</span>
      <span class="details__year">2015</span>
      <span class="details__small">750 ML</span>
    </div>
  </section>

  <section class="label label--white">
    <header class="brand">
      <h1 class="brand__name">MARROWIND</h1>
      <p class="brand__sub">ESTATES</p>
    </header>
    <div class="emblem" role="img" aria-label="Varietal emblem with small fairy mark"></div>
    <h2 class="varietal">CHARDONNAY</h2>
    <p class="region">VIRGINIA</p>
    <div class="details">
      <span class="details__small">13,1% VOL</span>
      <span class="details__year">2015</span>
      <span class="details__small">750 ML</span>
    </div>
  </section>
</body>
</html>
```